Luxury WordPress Website for CORALBASINS

I need a professional WordPress website for Coral Basins. The site should be modern, visually appealing, and user-friendly, reflecting the brand’s luxury and premium identity. It must include a homepage, product/service pages, contact form, and be responsive on both desktop and mobile devices. The design should allow for easy updates and integration of future content, while maintaining a polished and professional look.

Target Market(s)

swimmingpool & spa

Industry/Entity Type

Swimmingpool

Coding

Coded - Design and coding required

Font styles to use
Other font styles liked:
• HaboroSoft

Requirements
Must have
• Exclusive appearance
Nice to have
• • A logo that subtly incorporates water or pool elements. • A color palette that reflects luxury, elegance, and relaxation. • Clean and modern typography that is easy to read across all media. • Iconography or design elements that convey premium quality. • A versatile design that can be adapted for social media, merchandise, and promotional materials. • Optional: A tagline that emphasizes luxury and high-end pool experiences.

```html
<!DOCTYPE html>
<html lang="en">
<head>
<meta charset="UTF-8">
<title>Coral Basins — Pool design</title>
<link href="https://fonts.googleapis.com/css2?family=Archivo+Black&family=Nunito:wght@400;500;600;700;800&display=swap" rel="stylesheet">
<style>
  :root {
    --ink: #111827;
    --text: #374151;
    --muted: #4b5563;
    --line: #eef0f2;
    --teal: #3bb5d6;
    --green: #3bb36a;
    --chip: #f3f4f6;
    --bg: #ffffff;
    --visual-start: #2a5563;
    --visual-end: #2b3340;
  }
  * { box-sizing: border-box; margin: 0; padding: 0; }
  html, body { width: 1200px; height: 691px; overflow: hidden; background: var(--bg); }
  body { font-family: "Nunito", sans-serif; color: var(--ink); position: relative; }

  .site-header { position: absolute; left: 0; top: 0; width: 1200px; height: 64px; border-bottom: 1px solid var(--line); }
  .brand { position: absolute; left: 163px; top: 16px; display: flex; align-items: center; gap: 8px; }
  .brand-mark { width: 33px; height: 33px; border-radius: 5px; background: linear-gradient(135deg, var(--green), var(--teal)); }
  .brand-name { font-size: 13px; font-weight: 600; color: var(--ink); }
  .main-nav { position: absolute; left: 301px; top: 26px; display: flex; gap: 22px; font-size: 10px; color: var(--text); }
  .btn-header { position: absolute; left: 921px; top: 21px; width: 104px; height: 24px; border-radius: 4px; background: linear-gradient(90deg, var(--teal), var(--green)); color: #fff; font-size: 10px; font-weight: 700; display: flex; align-items: center; justify-content: center; }

  .hero-title { position: absolute; left: 163px; top: 112px; width: 360px; font-family: "Archivo Black", sans-serif; font-size: 34px; line-height: 42px; color: var(--ink); }
  .hero-lead { position: absolute; left: 163px; top: 253px; width: 400px; font-size: 12px; line-height: 20px; color: var(--text); }
  .btn { position: absolute; top: 314px; height: 35px; border-radius: 4px; font-size: 11px; font-weight: 700; display: flex; align-items: center; justify-content: center; }
  .btn-primary { left: 163px; width: 127px; background: linear-gradient(90deg, var(--teal), var(--green)); color: #fff; box-shadow: 0 3px 8px rgba(59,179,106,.25); }
  .btn-outline { left: 302px; width: 106px; border: 1px solid #cfe8ea; color: #1f4f5a; background: #fff; }

  .feature { position: absolute; top: 377px; display: flex; align-items: center; gap: 9px; }
  .feature-icon { width: 28px; height: 28px; border-radius: 4px; background: var(--chip); display: flex; align-items: center; justify-content: center; }
  .feature-label { font-size: 10px; color: var(--muted); line-height: 14px; }
  .feature-value { font-size: 11px; font-weight: 700; color: var(--ink); line-height: 16px; }

  .hero-visual { position: absolute; left: 609px; top: 124px; width: 416px; height: 269px; border-radius: 8px;
    background: linear-gradient(180deg, var(--visual-start) 0%, var(--visual-end) 100%);
    box-shadow: 0 12px 28px rgba(17,24,39,.18); }

  .section-title { position: absolute; left: 163px; top: 454px; font-size: 20px; font-weight: 600; color: var(--ink); }
</style>
</head>
<body>
  <header class="site-header">
    <div class="brand"><span class="brand-mark"></span><span class="brand-name">Coral Basins</span></div>
    <nav class="main-nav"><span>Home</span><span>Services</span><span>Portfolio</span><span>About</span><span>Contact</span></nav>
    <div class="btn-header">Book Consultation</div>
  </header>

  <h1 class="hero-title">Pool design that transforms outdoor living.</h1>
  <p class="hero-lead">We design, build and maintain premium swimming pools and spas — tailored to your property and lifestyle.</p>
  <div class="btn btn-primary">Book Consultation</div>
  <div class="btn btn-outline">View Portfolio</div>

  <div class="feature" style="left:163px">
    <div class="feature-icon"><svg width="11" height="11" viewBox="0 0 12 12"><path d="M2 6.5l2.5 2.5L10 3" fill="none" stroke="#111827" stroke-width="1.6"/></svg></div>
    <div><div class="feature-label">Certified builders</div><div class="feature-value">Expert team</div></div>
  </div>
  <div class="feature" style="left:325px">
    <div class="feature-icon"><svg width="11" height="11" viewBox="0 0 12 12"><circle cx="6" cy="6.5" r="4.3" fill="none" stroke="#6b7280" stroke-width="1"/><path d="M6 4v2.6M4.8 1.2h2.4" stroke="#6b7280" stroke-width="1"/></svg></div>
    <div><div class="feature-label">On-time delivery</div><div class="feature-value">Reliable process</div></div>
  </div>

  <div class="hero-visual" role="img" aria-label="Hero photograph of a night sky"></div>

  <h2 class="section-title">Our Services</h2>
</body>
</html>
```